Business Card Design

Hoping for a black background business card, minimalistic design.
With the Marble Crest logo you created in white.

I would like to include:
My Name and title
Address (street address)
Reception: (phone number)
Fax: (fax number)
Reception: (email address)
Direct email: (email address)
Instagram: (ig handle)

```html
<!DOCTYPE html>
<html lang="en">
<head>
<meta charset="UTF-8">
<title>Marble Crest — Business Card</title>
<link href="https://fonts.googleapis.com/css2?family=Montserrat:wght@300;400;500;600&display=swap" rel="stylesheet">
<style>
  :root {
    --stage: #161616;
    --card: #0e0e0e;
    --ink: #f2f2f2;
    --ink-soft: #cfcfcf;
  }
  * { margin: 0; padding: 0; box-sizing: border-box; }
  html, body { width: 1200px; height: 800px; overflow: hidden; background: var(--stage); }
  body { font-family: "Montserrat", sans-serif; color: var(--ink); position: relative; }

  .card {
    position: absolute;
    width: 520px;
    height: 298px;
    background: var(--card);
    border-radius: 22px;
    box-shadow: 0 14px 40px rgba(0,0,0,0.55);
  }
  .card--front { left: 340px; top: 70px; }
  .card--back  { left: 340px; top: 420px; }

  /* Front */
  .identity { position: absolute; left: 34px; top: 48px; }
  .identity__name { font-size: 17px; font-weight: 600; letter-spacing: 0.3px; }
  .identity__title { font-size: 10.5px; font-weight: 300; letter-spacing: 1px; margin-top: 3px; margin-left: 6px; color: var(--ink-soft); }

  .contact-list { position: absolute; left: 46px; top: 122px; list-style: none; font-size: 13px; font-weight: 300; line-height: 22px; }
  .contact-list__label { display: inline-block; width: 22px; }

  .address { position: absolute; left: 58px; top: 222px; font-size: 10px; font-weight: 400; line-height: 13px; color: var(--ink-soft); }

  .wordmark-large {
    position: absolute; right: 36px; top: 72px;
    font-size: 46px; font-weight: 600; line-height: 52px;
    letter-spacing: 3px; text-align: right; text-transform: uppercase;
  }

  /* Back */
  .brand-lockup { position: absolute; left: 46px; top: 62px; display: flex; align-items: center; gap: 20px; }
  .brand-lockup__ring { width: 88px; height: 88px; border: 4px solid var(--ink); border-radius: 50%; }
  .brand-lockup__divider { width: 1.5px; height: 78px; background: var(--ink); }
  .brand-lockup__name { font-size: 30px; font-weight: 500; letter-spacing: 3px; text-transform: uppercase; }

  .links { position: absolute; left: 170px; top: 198px; list-style: none; font-size: 13.5px; font-weight: 500; }
  .links__item { display: flex; align-items: center; gap: 10px; height: 30px; }
  .links__icon { width: 20px; height: 16px; display: block; }
  .links__dot { width: 18px; height: 18px; border: 2px solid var(--ink); border-radius: 5px; margin: 0 1px; }
</style>
</head>
<body>
  <section class="card card--front" aria-label="Business card front">
    <div class="identity">
      <p class="identity__name">MARBLE CREST</p>
      <p class="identity__title">FOUNDER</p>
    </div>
    <ul class="contact-list">
      <li><span class="contact-list__label">P :</span>+1 555 014 2290</li>
      <li><span class="contact-list__label">F :</span>+1 555 014 2291</li>
      <li><span class="contact-list__label">M:</span>hello@marblecrest.co</li>
    </ul>
    <address class="address" style="font-style:normal">
      48 Harbour Lane,<br>Westbrook, Kent, WB4 7QL
    </address>
    <p class="wordmark-large">Marble<br>Crest</p>
  </section>

  <section class="card card--back" aria-label="Business card back">
    <div class="brand-lockup">
      <span class="brand-lockup__ring"></span>
      <span class="brand-lockup__divider"></span>
      <span class="brand-lockup__name">Marble Crest</span>
    </div>
    <ul class="links">
      <li class="links__item">
        <svg class="links__icon" viewBox="0 0 20 16" aria-hidden="true">
          <rect x="0.5" y="1" width="19" height="14" rx="2" fill="#f2f2f2"/>
          <path d="M1.5 2.5 L10 9 L18.5 2.5" fill="none" stroke="#0e0e0e" stroke-width="1.8"/>
        </svg>
        studio@marblecrest.co
      </li>
      <li class="links__item">
        <span class="links__dot"></span>
        @marblecrest.studio
      </li>
    </ul>
  </section>
</body>
</html>
```